Lumo Vance IT company Soho london Stationary

We've just had a new logo designed on Gallow Pier and we now need some Stationary to go with it.
We're a small IT support firm supporting Design companies in Soho London. Most of our clients work on Vorls and a relatively creative so we want a relatively informal design on our stationary to reflect this.
We'd like to stick with the green in the logo but we're not adverse to adding another few colours to the palette.
Please see the attached file for our logo and not our website.

It Company

```html
<!DOCTYPE html>
<html lang="en">
<head>
<meta charset="utf-8">
<title>Lumo Vance Stationery</title>
<link href="https://fonts.googleapis.com/css2?family=Questrial&display=swap" rel="stylesheet">
<style>
  :root {
    --backdrop: #666666;
    --paper: #ffffff;
    --lime: #b4e61e;
    --ink: #111111;
    --band: #e2e2e2;
    --mark-faint: #e6e6e6;
    --edge: #d8d8d8;
  }
  * { margin: 0; padding: 0; box-sizing: border-box; }
  html, body { width: 862px; height: 1200px; overflow: hidden; }
  body { background: var(--backdrop); font-family: "Questrial", sans-serif; color: var(--lime); }

  .letterhead {
    position: absolute; left: 18px; top: 18px; width: 792px; height: 1122px;
    background: var(--paper);
  }
  .wordmark { position: absolute; display: flex; align-items: center; gap: 8px; color: var(--lime); white-space: nowrap; }
  .wordmark .dot { display: inline-block; border-radius: 50%; background: var(--lime); }

  .letterhead-mark { left: 476px; top: 48px; font-size: 40px; }
  .letterhead-mark .dot { width: 16px; height: 16px; }

  .letterhead-footer { position: absolute; left: 42px; top: 948px; font-size: 11px; line-height: 15px; letter-spacing: 0.5px; }
  .letterhead-footer p + p { margin-top: 15px; }
  .footer-emblem { position: absolute; left: 180px; top: 950px; width: 110px; height: 110px; border-radius: 50%; background: var(--mark-faint); }

  .card {
    position: absolute; background: var(--paper); border: 1px solid var(--edge); overflow: hidden;
  }
  .card-back { left: 140px; top: 155px; width: 345px; height: 205px; }
  .card-back .holder { position: absolute; left: 24px; top: 22px; font-size: 11px; line-height: 20px; }
  .card-back .holder .contact { margin-top: 14px; line-height: 16px; }
  .card-back .office { position: absolute; right: 14px; top: 30px; font-size: 10px; line-height: 15px; text-align: right; }
  .card-emblem { position: absolute; right: 22px; bottom: 16px; width: 100px; height: 100px; border-radius: 50%; background: var(--lime); }

  .card-front { left: 80px; top: 300px; width: 365px; height: 205px; }
  .card-front .wordmark { left: 80px; top: 68px; font-size: 34px; }
  .card-front .wordmark .dot { width: 14px; height: 14px; }
  .card-front .band { position: absolute; left: 0; right: 0; bottom: 0; height: 80px; background: var(--band); }
  .card-front .web { position: absolute; right: 16px; bottom: 14px; font-size: 13px; line-height: 18px; text-align: right; }

  .envelope { position: absolute; left: 66px; top: 520px; width: 702px; height: 300px; background: var(--paper); border: 1px solid var(--edge); }
  .envelope .wordmark { right: 70px; top: 34px; font-size: 30px; }
  .envelope .wordmark .dot { width: 12px; height: 12px; }
  .address-lines { position: absolute; left: 392px; top: 108px; width: 225px; }
  .address-lines span { display: block; height: 1px; background: var(--ink); margin-bottom: 32px; }
  .envelope-emblem { position: absolute; left: 34px; top: 80px; width: 80px; height: 80px; border-radius: 50%; background: var(--lime); }
  .envelope .sender { position: absolute; left: 48px; top: 180px; font-size: 10px; line-height: 14px; }
  .envelope .sender p + p { margin-top: 12px; }
</style>
</head>
<body>
  <main class="letterhead">
    <div class="wordmark letterhead-mark"><span>Lumo Vance</span><span class="dot"></span></div>

    <section class="card card-back">
      <div class="holder">
        <p>Name</p>
        <p>Designation</p>
        <div class="contact">
          <p>Mob 0000000000</p>
          <p>Email hello@lumovance.co</p>
        </div>
      </div>
      <address class="office" style="font-style:normal">Lumo Vance Ltd.<br>42 Corvin Row<br>London<br>W1X 7QP</address>
      <div class="card-emblem" aria-hidden="true"></div>
    </section>

    <section class="card card-front">
      <div class="wordmark"><span>Lumo Vance</span><span class="dot"></span></div>
      <div class="band"></div>
      <p class="web">Web: www.lumovance.co<br>email: info@lumovance.co</p>
    </section>

    <section class="envelope">
      <div class="wordmark"><span>Lumo Vance</span><span class="dot"></span></div>
      <div class="address-lines"><span></span><span></span></div>
      <div class="envelope-emblem" aria-hidden="true"></div>
      <address class="sender" style="font-style:normal">
        <p>Lumo Vance Ltd<br>42 Corvin Row<br>London<br>W1X 7QP</p>
        <p>Phone: 0203 555 0147<br>Web: http://lumovance.co<br>email: info@lumovance.co</p>
      </address>
    </section>

    <address class="letterhead-footer" style="font-style:normal">
      <p>Lumo Vance Ltd.<br>42 Corvin Row<br>London<br>W1X 7QP</p>
      <p>Phone: 0203 555 0147<br>Web: http://lumovance.co<br>email: info@lumovance.co</p>
    </address>
    <div class="footer-emblem" aria-hidden="true"></div>
  </main>
</body>
</html>
```